4 Business Card templates for printing site

I want 4 business card templates (including a front and a back). You should provide a variety of designs covering a cross section of industries. It is fine if this is taken from variations on designs of previous work that you have produced.

**All the designs can be provided in one file**

The templates will be used for a website I am building which is targeted at servicing printing requirements for micro businesses (small business with less than 10 people). The first product to be launched is business cards. I will require ~500 designs so this initial phase is partly to identify potential designers with the capability to produce a broad range of designs to populate the site.

For this project 4 templates are required in total.
I want 2 generic designs - designs that are not industry specific (just simple classic modern templates), one that would have room for a logo to be added and one that works well as a design without a logo.

The other 4 designs can be across any industry. These will be for business without logos that still want to have a flavour of what they do represented by the card. These can include illustrations or photos.

Below is a list of industries which the templates will cover: Accountancy, Finance,Advertising, PR, Animal & Pet Care, Architecture, Builders, Childcare, cleaning, Driving Instructors, Education & Training, Electrician,Fashion, Florist / gardening,Hairdresser, Legal, Medical & Dental, Music & DJ, Painter, photographer, Plumber, Real Estate & Property, Salons, Spas, Wellbeing & Beauty, Sports & Fitness, Trademen - carpenter, handyman, Wedding Event & Party Planing.

For inspiration below are some sites where examples of templates can be seen:

Graphic / illustrative templates:
http://uk.plindrow.com/design-templates/business-cards/
and example of industry specific such as a plumber:
http://uk.plindrow.com/design-templates/business-cards/?search=industry:%22DIY%20%26%20Tradesmen%22&advsearch=1&filters=1

Example of card design treatment with photo front and back
http://www.zorvani.com/product/518273/details.htm

and of course the biggest online printer (although design quality is not very high).
http://www.quelbarn.co.uk/gallery/QBXAAAACAAAAAAA=/premium-business-cards.aspx?xnav=HowToDesign

For designers that submit work that does not win, I will pay £20 for specific templates that I want to use on the site.

For the winning designs I will require SVG files.

Target Market(s)

Micro businesses (small business with less than 10 people). Often self employed people.

Industry/Entity Type

Printing

Requirements
Nice to have
• I want to see well balanced designs, which have good use of space, font, colour and graphics.
Should not have
• I do not want to see poor quality "clip art" style designs!

```html
<!DOCTYPE html>
<html lang="en">
<head>
<meta charset="utf-8">
<title>Business Card Template – Interiors &amp; Flooring</title>
<link rel="stylesheet" href="https://fonts.googleapis.com/css2?family=Gelasio:wght@400&display=swap">
<style>
  :root {
    --stage: #5a5a5a;
    --olive: #9b9448;
    --olive-shadow: #4a4630;
    --ink-light: #ffffff;
    --ink-dark: #5d592b;
    --room-light: #e6ddd0;
    --room-mid: #c9b9a3;
    --room-floor: #c8a980;
    --carpet-light: #a59a92;
    --carpet-dark: #6f645d;
  }
  * { margin: 0; padding: 0; box-sizing: border-box; }
  html, body {
    width: 1200px; height: 597px; overflow: hidden;
    background: var(--stage);
    font-family: "Gelasio", Georgia, serif;
  }
  .stage { position: relative; width: 1200px; height: 597px; }
  .card { position: absolute; overflow: hidden; }
  .card svg { position: absolute; left: 0; top: 0; display: block; }
  .card-back  { left: 544px; top: 6px;   width: 650px; height: 360px; }
  .card-front { left: 0;     top: 211px; width: 684px; height: 379px; }

  .text { position: absolute; white-space: nowrap; line-height: 1; }
  .light { color: var(--ink-light); }
  .dark  { color: var(--ink-dark); }

  /* back */
  .card-back .company-name    { left: 0; width: 616px; text-align: center; top: 12px; font-size: 34px; }
  .card-back .company-message { left: 0; width: 616px; text-align: center; top: 51px; font-size: 23px; }
  .card-back .website         { left: 0; width: 616px; text-align: center; top: 120px; font-size: 22px; }

  /* front */
  .card-front .company-name    { left: 13px; top: 12px; font-size: 35px; }
  .card-front .company-message { left: 13px; top: 54px; font-size: 23px; }
  .card-front .full-name       { left: 13px; top: 119px; font-size: 24px; }
  .card-front .job-title       { left: 13px; top: 150px; font-size: 20px; }
  .card-front .contact {
    position: absolute; left: 492px; top: 18px; list-style: none;
    font-size: 21px; line-height: 29px; color: var(--ink-dark);
  }
  .card-front .website { left: 232px; top: 197px; font-size: 22px; }
</style>
</head>
<body>
<main class="stage">

  <section class="card card-back" aria-label="Business card back">
    <svg width="650" height="360" viewBox="0 0 650 360">
      <defs>
        <linearGradient id="back-room" x1="0" y1="0" x2="0" y2="1">
          <stop offset="0" stop-color="var(--room-light)"/>
          <stop offset="0.55" stop-color="var(--room-mid)"/>
          <stop offset="1" stop-color="var(--room-floor)"/>
        </linearGradient>
        <linearGradient id="back-carpet" x1="0" y1="0" x2="1" y2="1">
          <stop offset="0" stop-color="var(--carpet-light)"/>
          <stop offset="1" stop-color="var(--carpet-dark)"/>
        </linearGradient>
      </defs>
      <rect x="0" y="190" width="419" height="170" fill="url(#back-room)" role="img" aria-label="Photo of a bright living room with armchairs and wooden floor"/>
      <rect x="419" y="190" width="231" height="170" fill="url(#back-carpet)" role="img" aria-label="Close-up photo of textured loop-pile carpet"/>
      <path d="M0 194 Q325 226 650 222 V232 Q325 236 0 206 Z" fill="var(--olive-shadow)" opacity="0.6"/>
      <path d="M0 0 H650 V220 Q325 222 0 194 Z" fill="var(--olive)"/>
    </svg>
    <p class="text light company-name">Company Name</p>
    <p class="text dark company-message">Company Message</p>
    <p class="text dark website">www.yoursite.com</p>
  </section>

  <section class="card card-front" aria-label="Business card front">
    <svg width="684" height="379" viewBox="0 0 684 379">
      <defs>
        <linearGradient id="front-room" x1="0" y1="0" x2="0" y2="1">
          <stop offset="0" stop-color="var(--room-light)"/>
          <stop offset="0.5" stop-color="var(--room-mid)"/>
          <stop offset="1" stop-color="var(--room-floor)"/>
        </linearGradient>
        <linearGradient id="front-carpet" x1="0" y1="0" x2="1" y2="1">
          <stop offset="0" stop-color="var(--carpet-light)"/>
          <stop offset="1" stop-color="var(--carpet-dark)"/>
        </linearGradient>
      </defs>
      <rect x="0" y="196" width="441" height="183" fill="url(#front-room)" role="img" aria-label="Photo of living room interiors with sofa, armchairs and fireplace"/>
      <rect x="441" y="196" width="243" height="183" fill="url(#front-carpet)" role="img" aria-label="Close-up photo of textured loop-pile carpet"/>
      <path d="M0 200 Q342 230 684 232 V242 Q342 240 0 212 Z" fill="var(--olive-shadow)" opacity="0.6"/>
      <path d="M0 0 H684 V232 Q342 228 0 200 Z" fill="var(--olive)"/>
    </svg>
    <p class="text light company-name">Company Name</p>
    <p class="text dark company-message">Company Message</p>
    <p class="text light full-name">Full Name</p>
    <p class="text dark job-title">Job Title</p>
    <ul class="contact">
      <li>Address Line 1</li>
      <li>Address Line 2</li>
      <li>Address Line 3</li>
      <li>Phone/Other</li>
      <li>Email/Other</li>
    </ul>
    <p class="text dark website">www.yoursite.com</p>
  </section>

</main>
</body>
</html>
```